Business card design needed

I am a musculoskeletal therapist and pride myself in offering a top service. The market is very competitive and therefore the card needs to reflect professionalism and trust.

Industry/Entity Type

Business

Contact Information for Business Card

Business: Balanced Kinetics
Message: Muscle, Nerve & Joint Pain Management
Name: Laurent Dubreuil
Title: Remedial Therapist
Phone: 0471 586 209
Display: Nice anatomical image of a body targeting/circling the muscle, spine and nerve in 3 circles. Next to the image a logo with the letters BK.

```html
<!DOCTYPE html>
<html lang="en">
<head>
<meta charset="utf-8">
<title>Balanced Kinetics – Business Card</title>
<link rel="stylesheet" href="https://fonts.googleapis.com/css2?family=Montserrat:wght@500;600;700&family=Dancing+Script:wght@600&display=swap">
<style>
  :root {
    --page-bg: #e9e6e1;
    --card-light: #27a6e4;
    --card-mid: #1f72cc;
    --card-deep: #2b3598;
    --tab-bg: rgba(24, 40, 120, 0.55);
    --white: #ffffff;
    --soft-white: rgba(255, 255, 255, 0.88);
    --mark-faint: rgba(255, 255, 255, 0.16);
    --anatomy-top: #8fcff0;
    --anatomy-mid: #c79a98;
    --anatomy-low: #d8735a;
  }
  * { box-sizing: border-box; margin: 0; padding: 0; }
  html, body {
    width: 1200px;
    height: 740px;
    overflow: hidden;
    background: var(--page-bg);
  }
  .canvas {
    position: relative;
    width: 1200px;
    height: 740px;
  }
  .business-card {
    position: absolute;
    left: 75px;
    top: 70px;
    width: 1050px;
    height: 600px;
    overflow: hidden;
    background: linear-gradient(115deg, var(--card-light) 0%, var(--card-mid) 45%, var(--card-deep) 100%);
    box-shadow: 0 10px 30px rgba(0, 0, 0, 0.18);
  }
  .anatomy-illustration {
    position: absolute;
    left: 0;
    top: 0;
    width: 330px;
    height: 600px;
    background: linear-gradient(180deg, var(--anatomy-top) 0%, var(--anatomy-mid) 50%, var(--anatomy-low) 100%);
    -webkit-mask-image: linear-gradient(90deg, #000 70%, transparent 100%);
    mask-image: linear-gradient(90deg, #000 70%, transparent 100%);
  }
  .contact-tab {
    position: absolute;
    top: 0;
    right: 0;
    width: 300px;
    padding: 18px 24px 16px 26px;
    background: var(--tab-bg);
    border-bottom-left-radius: 22px;
    color: var(--white);
  }
  .contact-tab .person-name {
    font-family: "Montserrat", sans-serif;
    font-weight: 700;
    font-size: 22px;
    letter-spacing: 0.2px;
  }
  .contact-tab .person-title {
    font-family: "Dancing Script", cursive;
    font-weight: 600;
    font-size: 19px;
    margin-top: 2px;
    color: var(--soft-white);
  }
  .contact-tab .person-phone {
    font-family: "Montserrat", sans-serif;
    font-weight: 500;
    font-size: 17px;
    margin-top: 2px;
    color: var(--soft-white);
  }
  .brand-lockup {
    position: absolute;
    left: 355px;
    top: 200px;
    display: flex;
    align-items: center;
    gap: 22px;
  }
  .brand-square {
    width: 96px;
    height: 96px;
    border-radius: 14px;
    background: var(--white);
    flex: none;
  }
  .brand-text .business-name {
    font-family: "Montserrat", sans-serif;
    font-weight: 600;
    font-size: 46px;
    font-variant: small-caps;
    letter-spacing: 1.5px;
    color: var(--white);
    line-height: 1;
  }
  .brand-text .tagline {
    font-family: "Montserrat", sans-serif;
    font-weight: 700;
    font-size: 19px;
    font-variant: small-caps;
    letter-spacing: 0.6px;
    color: var(--white);
    margin-top: 10px;
  }
  .corner-mark {
    position: absolute;
    right: 40px;
    bottom: 90px;
    width: 170px;
    height: 170px;
    border-radius: 26px;
    background: var(--mark-faint);
  }
</style>
</head>
<body>
  <main class="canvas">
    <section class="business-card">
      <div class="anatomy-illustration" role="img" aria-label="Anatomical illustration of a human back and shoulder seen from behind, with the spine, muscles and nerves highlighted"></div>

      <div class="contact-tab">
        <p class="person-name">Laurent Dubreuil</p>
        <p class="person-title">Remedial Therapist</p>
        <p class="person-phone">Ph. 0471 586 209</p>
      </div>

      <div class="brand-lockup">
        <div class="brand-square"></div>
        <div class="brand-text">
          <h1 class="business-name">Balanced Kinetics</h1>
          <p class="tagline">Muscle, Nerve &amp; Joint Pain Management</p>
        </div>
      </div>

      <div class="corner-mark"></div>
    </section>
  </main>
</body>
</html>
```